Flyer for the Harvest Lantern Gathering 2018

Design a flyer for our annual conference with basic information about the conference: conference logo and year,

Location:
Dunmore Community Center (Downtown Portland)
482 Willowby Street, Portland, ME 04117,

Date:
August 24th, 25th and 26th, 2018
Start time 6:00PM

I would like the following three words added to the flyer. These words describe the vision of the conference:
Prophetic, Worship, Prayer

```html
<!DOCTYPE html>
<html lang="en">
<head>
<meta charset="utf-8">
<title>Harvest Lantern Gathering 2018</title>
<link href="https://fonts.googleapis.com/css2?family=Cinzel:wght@400;700;900&display=swap" rel="stylesheet">
<style>
  :root {
    --paper-light: #f1f1f1;
    --paper-mid: #dcdcdc;
    --paper-dark: #c4c4c4;
    --ink: #111111;
    --gold-light: #c99a22;
    --gold-mid: #8a6410;
    --gold-dark: #3d2a05;
    --badge-bg: #000000;
    --badge-edge: #c8961e;
    --ornament: #8d8d8d;
  }
  html, body {
    margin: 0;
    padding: 0;
    overflow: hidden;
    background: var(--paper-mid);
  }
  .flyer {
    position: relative;
    width: 880px;
    height: 1200px;
    overflow: hidden;
    background:
      radial-gradient(ellipse at 50% 40%, var(--paper-light) 0%, var(--paper-mid) 60%, var(--paper-dark) 100%);
    font-family: "Cinzel", serif;
    color: var(--ink);
  }
  .badge {
    position: absolute;
    left: 379px;
    top: 0;
    width: 122px;
    height: 140px;
    box-sizing: border-box;
    background: var(--badge-bg);
    border: 2px solid var(--badge-edge);
    border-top: none;
    display: flex;
    flex-direction: column;
    align-items: center;
    justify-content: center;
    gap: 10px;
  }
  .badge-mark {
    width: 58px;
    height: 58px;
    border-radius: 50%;
    border: 3px solid var(--badge-edge);
    box-sizing: border-box;
  }
  .badge-name {
    font-family: "Cinzel", serif;
    font-weight: 700;
    font-size: 15px;
    letter-spacing: 1px;
    color: var(--badge-edge);
  }
  .vision-word, .info {
    position: absolute;
    left: 0;
    width: 100%;
    text-align: center;
    line-height: 1;
    margin: 0;
    white-space: nowrap;
  }
  .vision-word {
    font-weight: 900;
    font-size: 76px;
    letter-spacing: -1px;
    background: linear-gradient(180deg, var(--gold-dark) 0%, var(--gold-mid) 40%, var(--gold-light) 60%, var(--gold-dark) 100%);
    -webkit-background-clip: text;
    background-clip: text;
    color: transparent;
    -webkit-text-stroke: 0.6px var(--gold-light);
  }
  .vision-prophetic { top: 236px; }
  .vision-worship { top: 534px; }
  .vision-prayer { top: 808px; }
  .info {
    font-weight: 400;
    font-size: 28px;
  }
  .info-venue { top: 372px; font-size: 25px; }
  .info-address { top: 408px; font-size: 26px; }
  .info-date { top: 650px; }
  .info-time { top: 916px; }
  .ornament {
    position: absolute;
    left: 352px;
    width: 156px;
    height: 60px;
    border-radius: 30px;
    background: radial-gradient(ellipse at center, var(--ornament) 0%, rgba(141,141,141,0.35) 55%, rgba(141,141,141,0) 75%);
  }
  .ornament-upper { top: 464px; }
  .ornament-lower { top: 720px; }
</style>
</head>
<body>
<main class="flyer">
  <div class="badge">
    <div class="badge-mark"></div>
    <div class="badge-name">LANTERN</div>
  </div>

  <h1 class="vision-word vision-prophetic">PROPHETIC</h1>

  <p class="info info-venue">Dunmore Community Center (Downtown Portland)</p>
  <p class="info info-address">482 Willowby Street, Portland, ME 04117,</p>

  <div class="ornament ornament-upper" role="img" aria-label="Grey floral flourish divider"></div>

  <h2 class="vision-word vision-worship">Worship</h2>

  <p class="info info-date">August 24th, 25th and 26th, 2018</p>

  <div class="ornament ornament-lower" role="img" aria-label="Grey floral flourish divider"></div>

  <h2 class="vision-word vision-prayer">Prayer</h2>

  <p class="info info-time">Start time 6:00PM</p>
</main>
</body>
</html>
```